Corporate consulting business needs a business card

I want a professional business card.... surprise me

Target Market(s)

Corprorate and Not for Profit firms and organisations

Industry/Entity Type

Consulting

Contact Information for Business Card

Logo
Corporate Consulting Services
On Time, On Budget, Beyond Expectation
Tobin Averley
Director
0427 31 64 92 (Larger)
tobin@ta-advisory.com.au
www.ta-advisory.com.au
include little icons beside the contact info:

- Envelope = email
- Phone = phone
- Globe = website

Font styles to use
Serif
Sans Serif

Requirements
Must have
• Professional and clean
Nice to have
• you tell me

```html
<!DOCTYPE html>
<html lang="en">
<head>
<meta charset="utf-8">
<title>TA Advisory Services – Business Card</title>
<link rel="stylesheet" href="https://fonts.googleapis.com/css2?family=Cinzel:wght@400;600&family=Lato:wght@400&display=swap">
<style>
  :root {
    --backdrop: #3e3e40;
    --brown: #4f2f1b;
    --paper: #ffffff;
    --stone: #dcd8d2;
    --ink: #2a1a10;
    --grey-text: #7a7a7a;
    --white: #ffffff;
  }
  * { margin: 0; padding: 0; box-sizing: border-box; }
  html, body { width: 1200px; height: 810px; overflow: hidden; }
  body { background: var(--backdrop); position: relative; font-family: "Lato", sans-serif; }

  .card {
    position: absolute;
    width: 600px;
    height: 343px;
    border-radius: 18px;
    overflow: hidden;
    box-shadow: 0 10px 24px rgba(0,0,0,0.35);
  }

  /* Back of card */
  .card--back { left: 100px; top: 50px; background: var(--brown); }
  .card--back .brand {
    position: absolute; left: 0; right: 0; top: 118px;
    display: flex; align-items: center; justify-content: center; gap: 16px;
  }
  .brand__ring {
    width: 46px; height: 46px; border-radius: 50%;
    border: 2px solid currentColor; flex: none;
  }
  .brand__name {
    font-family: "Cinzel", serif; font-weight: 600;
    letter-spacing: 1.5px; white-space: nowrap;
  }
  .card--back .brand { color: var(--stone); }
  .card--back .brand__name { font-size: 26px; }
  .tagline {
    position: absolute; left: 0; right: 0; top: 238px;
    text-align: center; color: var(--white); font-size: 17px; letter-spacing: 0.3px;
  }

  /* Front of card */
  .card--front { left: 500px; top: 417px; background: var(--paper); }
  .card--front .brand {
    position: absolute; left: 36px; top: 110px;
    display: flex; align-items: center; gap: 12px; color: var(--brown);
  }
  .card--front .brand__ring { width: 40px; height: 40px; }
  .card--front .brand__name { font-size: 15px; letter-spacing: 1px; color: var(--ink); }
  .divider {
    position: absolute; left: 312px; top: 62px; width: 1px; height: 120px;
    background: linear-gradient(var(--brown), rgba(79,47,27,0));
  }
  .contact { position: absolute; left: 336px; top: 66px; }
  .contact__name {
    font-family: "Cinzel", serif; font-weight: 600; font-size: 22px;
    color: var(--brown); letter-spacing: 0.5px; white-space: nowrap;
  }
  .contact__role { font-size: 15px; color: var(--grey-text); margin-top: 2px; }
  .contact__list { list-style: none; margin-top: 22px; }
  .contact__item {
    display: flex; align-items: center; gap: 9px; white-space: nowrap;
    font-size: 13.5px; color: var(--grey-text); margin-bottom: 6px;
  }
  .contact__item svg { width: 13px; height: 13px; flex: none; }
  .band { position: absolute; left: 0; bottom: 0; width: 600px; height: 80px; }
  .phone {
    position: absolute; left: 30px; bottom: 12px;
    display: flex; align-items: center; gap: 10px;
    font-family: "Cinzel", serif; font-size: 31px; color: var(--white); letter-spacing: 1px;
  }
  .phone svg { width: 22px; height: 22px; fill: var(--white); }
</style>
</head>
<body>

<section class="card card--back">
  <div class="brand">
    <span class="brand__ring"></span>
    <span class="brand__name">TA Advisory Services</span>
  </div>
  <p class="tagline">• On Time • On Budget • Beyond Expectation</p>
</section>

<section class="card card--front">
  <div class="brand">
    <span class="brand__ring"></span>
    <span class="brand__name">TA Advisory Services</span>
  </div>

  <div class="divider"></div>

  <div class="contact">
    <h1 class="contact__name">TOBIN AVERLEY</h1>
    <p class="contact__role">Director</p>
    <ul class="contact__list">
      <li class="contact__item">
        <svg viewBox="0 0 16 16" aria-hidden="true"><path d="M1 3h14v10H1z M1.5 3.5 8 9l6.5-5.5" fill="none" stroke="#2a1a10" stroke-width="1.6"/></svg>
        tobin@ta-advisory.com.au
      </li>
      <li class="contact__item">
        <svg viewBox="0 0 16 16" aria-hidden="true"><circle cx="8" cy="8" r="6.5" fill="none" stroke="#2a1a10" stroke-width="1.4"/><path d="M1.5 8h13M8 1.5c-3 3.5-3 9.5 0 13M8 1.5c3 3.5 3 9.5 0 13" fill="none" stroke="#2a1a10" stroke-width="1.2"/></svg>
        www.ta-advisory.com.au
      </li>
    </ul>
  </div>

  <svg class="band" viewBox="0 0 600 80" preserveAspectRatio="none" aria-hidden="true">
    <polygon points="0,20 360,20 378,30 600,30 600,36 380,36" fill="var(--stone)"/>
    <polygon points="0,20 330,20 360,34 600,34 600,80 0,80" fill="var(--brown)"/>
  </svg>
  <div class="phone">
    <svg viewBox="0 0 24 24" aria-hidden="true"><path d="M6.6 10.8a15.2 15.2 0 0 0 6.6 6.6l2.2-2.2a1 1 0 0 1 1-.25 11.4 11.4 0 0 0 3.6.57 1 1 0 0 1 1 1V20a1 1 0 0 1-1 1A17 17 0 0 1 3 4a1 1 0 0 1 1-1h3.5a1 1 0 0 1 1 1c0 1.25.2 2.45.57 3.6a1 1 0 0 1-.25 1z"/></svg>
    0427 31 64 92
  </div>
</section>

</body>
</html>
```